Amber Meadow LLC business card

I help with the Marketing and Sales of various Natural, Organic, Eco Friendly and Healthy Main Stream products to Retail Corporate accounts as well as Independents and Distributors.I also highlight Private label items to these same Retail Corporate accounts.Savor Each Day, Live Gently!

Speciality & Health Sales and Marketing

Target Market(s)

Men and Women

Industry/Entity Type

Business

Contact Information for Business Card

Amber Meadow, LLC
Lydia Rose Vandermeer
427 West Orchard Lane
Ste 5-384
Phoenix, AZ 85317
602-718-3054
lvandermeer@pinemail.net

Requirements
Must have
• Nice, femine font
Something in the background or on a side with a softness
Nice to have
• Cherish the Moments, Enjoy Life
Should not have
• Hardness

```html
<!DOCTYPE html>
<html lang="en">
<head>
<meta charset="UTF-8">
<title>Amber Meadow, LLC — Business Card</title>
<link href="https://fonts.googleapis.com/css2?family=League+Script&family=Quicksand:wght@400;500&display=swap" rel="stylesheet">
<style>
  :root {
    --page-bg: #f3eeea;
    --card-light: #f1cfe0;
    --card-mid: #e6a9c9;
    --card-deep: #dd8fb9;
    --ink: #ffffff;
    --icon-cut: #e3a2c5;
    --shadow: rgba(120, 60, 90, 0.22);
  }
  * { margin: 0; padding: 0; box-sizing: border-box; }
  html, body {
    width: 1200px;
    height: 800px;
    overflow: hidden;
    background: var(--page-bg);
  }
  .stage {
    width: 1200px;
    height: 800px;
    display: flex;
    align-items: center;
    justify-content: center;
  }
  .business-card {
    position: relative;
    width: 900px;
    height: 514px;
    border-radius: 22px;
    background: linear-gradient(100deg, var(--card-light) 0%, var(--card-mid) 55%, var(--card-deep) 100%);
    box-shadow: 0 18px 40px var(--shadow);
    color: var(--ink);
    overflow: hidden;
  }
  .company-name {
    position: absolute;
    left: 42px;
    top: 30px;
    font-family: "League Script", cursive;
    font-weight: 400;
    font-size: 52px;
    line-height: 1.2;
    letter-spacing: 2px;
    white-space: nowrap;
  }
  .person-name {
    position: absolute;
    left: 44px;
    top: 104px;
    font-family: "Quicksand", sans-serif;
    font-weight: 500;
    font-size: 25px;
    line-height: 1.2;
    letter-spacing: 0.5px;
  }
  .contact-list {
    position: absolute;
    left: 236px;
    top: 168px;
    list-style: none;
    font-family: "Quicksand", sans-serif;
    font-weight: 500;
    font-size: 22px;
    line-height: 1.55;
    letter-spacing: 0.5px;
  }
  .contact-item {
    display: flex;
    align-items: flex-start;
    gap: 16px;
    margin-bottom: 8px;
  }
  .contact-icon {
    flex: 0 0 22px;
    width: 22px;
    height: 22px;
    margin-top: 6px;
  }
  .tagline {
    position: absolute;
    right: 48px;
    bottom: 44px;
    font-family: "League Script", cursive;
    font-weight: 400;
    font-size: 48px;
    line-height: 1.2;
    letter-spacing: 2px;
    white-space: nowrap;
  }
</style>
</head>
<body>
<main class="stage">
  <article class="business-card">
    <h1 class="company-name">Amber Meadow, LLC</h1>
    <p class="person-name">Lydia Rose Vandermeer</p>

    <ul class="contact-list">
      <li class="contact-item">
        <svg class="contact-icon" viewBox="0 0 24 24" aria-hidden="true">
          <path d="M12 2a7 7 0 0 0-7 7c0 5 7 13 7 13s7-8 7-13a7 7 0 0 0-7-7z" fill="#fff"/>
          <circle cx="12" cy="9" r="2.6" fill="var(--icon-cut)"/>
        </svg>
        <span>427 West Orchard Lane Ste 5-384 Phoenix,<br>AZ 85317</span>
      </li>
      <li class="contact-item">
        <svg class="contact-icon" viewBox="0 0 24 24" aria-hidden="true">
          <circle cx="12" cy="12" r="10" fill="none" stroke="#fff" stroke-width="2"/>
          <path d="M8.5 7.5l2 2-1.2 1.4c.8 1.6 1.8 2.6 3.4 3.4l1.4-1.2 2 2-1.3 1.4c-3.4-.3-7.3-4.2-7.6-7.6z" fill="#fff"/>
        </svg>
        <span>602-718-3054</span>
      </li>
      <li class="contact-item">
        <svg class="contact-icon" viewBox="0 0 24 24" aria-hidden="true">
          <circle cx="12" cy="12" r="11" fill="#fff"/>
          <rect x="6.5" y="8" width="11" height="8" rx="1" fill="var(--icon-cut)"/>
          <path d="M6.8 8.4L12 12.4l5.2-4" fill="none" stroke="#fff" stroke-width="1.4"/>
        </svg>
        <span>lvandermeer@pinemail.net</span>
      </li>
    </ul>

    <p class="tagline">Savor Each Day, Live Gently!</p>
  </article>
</main>
</body>
</html>
```